Corvell Tarn manufacturing Project

We are looking at getting a brand new design for a new company that deals in selling stainless tubing and other stainless still products such as handrails, Spigots, Balustrade Fittings
Glass, Glass fittings and Aluminium Channels

We require a very clean website that deals with the following colours:

Blue to light blues
Blacks
Greys to light Greys
Whites

We are open for other ideas BUT we *DO NOT* want any pinks, greens or bright colours except for backgrounds colours we have chosen above. (It can be solid, gradient or a subtle pattern)

YOU MUST KEEP THE LOGO AS IS. PLEASE DO NOT ALTER THE LOGO IN *ANY WAY* and the logo MUST be the same colours and fonts.

Logo is attached.

The site must contain these aspects:
jQuery Slider (Image slide show)
Top drop down Menus
Be no more than 900px wide
Text is to be to the k9R standards. (no special fonts)

We will chop up the design into html format. You just need to provide the PSD file.

The clients opposition is:
www.polbrenwick.com

It Company

• Alter the logo in anyway

```html
<!DOCTYPE html>
<html lang="en">
<head>
<meta charset="utf-8">
<title>Corvell Tarn Manufacturing</title>
<link href="https://fonts.googleapis.com/css2?family=PT+Sans+Narrow:wght@400;700&family=Source+Sans+3:wght@300;400;600&display=swap" rel="stylesheet">
<style>
:root{
  --navy:#3d4a78;
  --nav-top:#7f90bb;
  --nav-bottom:#53679a;
  --blue-btn:#6a80b8;
  --band-top:#ffffff;
  --band-bottom:#d8def0;
  --slide-bg:#b3b5bd;
  --frame:#eeeff2;
  --text:#3f4250;
  --grey-line:#c7cbd6;
  --footer:#5b5c5f;
  --footer-text:#ffffff;
  --caption:rgba(90,92,100,.55);
}
*{margin:0;padding:0;box-sizing:border-box}
html,body{width:1200px;height:1065px;overflow:hidden;background:#fff}
body{position:relative;font-family:"Source Sans 3",Arial,sans-serif;color:var(--text)}
.abs{position:absolute}

/* header */
.brand{left:186px;top:5px;width:150px;text-align:center}
.brand-mark{width:82px;height:82px;border-radius:50%;background:#2a2c33;border:5px solid #b9bcc6;margin:0 auto}
.brand-name{font-size:15px;font-weight:400;color:#222;margin-top:6px;line-height:1}
.brand-sub{font-size:7px;letter-spacing:1.3px;color:#222;margin-top:2px}

.catalogue{left:669px;top:11px;width:180px;height:38px;border-radius:3px;
  background:linear-gradient(#d8dadf,#aeb1b8);border:1px solid #9c9fa6;
  font-family:"PT Sans Narrow",sans-serif;font-weight:700;font-size:17px;color:#fff;
  display:flex;align-items:center;padding-left:11px;gap:9px;text-shadow:0 1px 1px rgba(0,0,0,.35)}
.search{left:858px;top:12px;width:154px;height:35px;border:1px solid #cfd1d6;border-radius:3px;
  background:linear-gradient(#fff,#f1f2f4);font-size:12px;color:#444;padding:10px 9px}
.search svg{position:absolute;right:8px;top:8px}

.nav{left:484px;top:69px;width:528px;height:40px;display:flex;border-radius:3px;overflow:hidden;
  background:linear-gradient(var(--nav-top),var(--nav-bottom));box-shadow:0 2px 3px rgba(0,0,0,.25)}
.nav a{display:flex;align-items:center;justify-content:center;color:#fff;text-decoration:none;
  font-family:"PT Sans Narrow",sans-serif;font-size:17px;border-right:1px solid #44568a}
.nav a:last-child{border-right:none}

/* slider */
.band{left:0;top:439px;width:1200px;height:528px;background:linear-gradient(var(--band-top),var(--band-bottom))}
.slider{left:194px;top:127px;width:818px;height:305px;background:var(--frame);border-radius:3px}
.slide{left:8px;top:8px;width:801px;height:290px;border-radius:3px;overflow:hidden;
  background:linear-gradient(90deg,var(--slide-bg) 0%,#b5b6bc 45%,#d6d5d3 75%,#c9c8c6 100%)}
.slide-photo{position:absolute;right:0;top:0;width:470px;height:290px;
  background:radial-gradient(ellipse at 60% 40%,rgba(235,235,235,.85),rgba(150,150,155,0) 70%),
  linear-gradient(160deg,rgba(255,255,255,0),rgba(120,120,125,.25))}
.slide h1{position:absolute;left:44px;top:50px;font-weight:300;font-size:51px;color:var(--navy);letter-spacing:.5px}
.slide p{position:absolute;left:45px;top:124px;width:320px;font-size:14px;line-height:21px;color:#333}
.read{position:absolute;left:45px;top:168px;width:90px;height:30px;border-radius:3px;
  background:linear-gradient(#7c90c6,#5b70ad);color:#fff;font-size:13px;display:flex;align-items:center;justify-content:center;
  box-shadow:0 1px 2px rgba(0,0,0,.3)}
.dots{position:absolute;left:48px;top:243px;display:flex;gap:5px}
.dots span{width:15px;height:15px;border-radius:50%;background:#fff;border:1px solid #999}
.dots span.on{background:radial-gradient(#7f95cc 40%,#fff 45%)}

/* product tiles */
.tile{width:263px;height:152px;border:1px solid #b5b8c0;overflow:hidden}
.tile .photo{position:absolute;inset:0}
.tile .cap{position:absolute;left:0;right:0;bottom:0;height:35px;background:var(--caption);
  display:flex;align-items:center;justify-content:space-between;padding:0 8px 0 11px}
.tile .cap b{font-weight:400;font-size:19px;color:#fff}
.tile .cap i{font-style:normal;font-size:14px;background:#fff;color:#444;padding:2px 6px}

/* welcome */
.welcome{left:195px;top:784px;width:817px;height:171px;border:1px solid var(--grey-line);
  background:linear-gradient(#fff,#e6eaf5)}
.welcome h2{position:absolute;left:19px;top:20px;font-weight:400;font-size:20px;color:#4d5b8c}
.welcome p{position:absolute;left:19px;top:51px;width:460px;font-size:12.6px;line-height:21.2px;text-align:justify;color:#3d3f48}
.people{left:496px;top:41px;width:310px;height:129px;
  background:linear-gradient(90deg,rgba(215,200,185,.6),rgba(245,240,235,.9) 45%,rgba(200,205,220,.6))}

/* footer */
.footer{left:0;top:967px;width:1200px;height:98px;background:var(--footer);border-top:3px solid #e6e8ee}
.footer-links{left:194px;top:22px;font-size:12px;color:var(--footer-text)}
.footer-links span{margin:0 7px;color:#ddd}
.copy{left:194px;top:44px;font-size:12px;color:var(--footer-text)}
.follow{right:188px;top:22px;font-size:12px;color:var(--footer-text)}
.social{right:186px;top:46px;display:flex;gap:6px}
.social span{width:24px;height:24px;border-radius:50%;background:linear-gradient(#a9b4d2,#6f7fa8);border:1px solid #3e4555}
</style>
</head>
<body>

<header>
  <div class="abs brand">
    <div class="brand-mark"></div>
    <div class="brand-name">Corvell Tarn</div>
    <div class="brand-sub">Manufacturing Co. Ltd</div>
  </div>

  <div class="abs catalogue">Download Catelogue
    <svg width="20" height="20" viewBox="0 0 20 20"><path d="M7 2h6v7h4l-7 7-7-7h4z" fill="#6b6e75"/><rect x="2" y="17" width="16" height="2" fill="#6b6e75"/></svg>
  </div>
  <div class="abs search">Search
    <svg width="16" height="16" viewBox="0 0 16 16"><circle cx="6" cy="6" r="4" fill="none" stroke="#555" stroke-width="2"/><path d="M9 9l5 5" stroke="#555" stroke-width="2.5"/></svg>
  </div>

  <nav class="abs nav">
    <a style="width:99px">Home</a>
    <a style="width:103px">About Us</a>
    <a style="width:104px">Products</a>
    <a style="width:109px">Download</a>
    <a style="width:113px">Contact Us</a>
  </nav>
</header>

<div class="abs band"></div>

<section class="abs slider">
  <div class="abs slide">
    <div class="slide-photo" role="img" aria-label="Photo of a stainless steel handrail with wall bracket"></div>
    <h1>Handrails</h1>
    <p>Lorem Ipsum is simply dummy text of the printing and typesetting industry.</p>
    <div class="read">READ MORE</div>
    <div class="dots"><span></span><span class="on"></span><span></span><span></span></div>
  </div>
</section>

<section>
  <div class="abs tile" style="left:194px;top:454px">
    <div class="photo" role="img" aria-label="Photo of stainless pool ladder handrails" style="background:linear-gradient(#9aa6d8,#6d7184 60%,#4c4e58)"></div>
    <div class="cap"><b>Handrails</b><i>MORE</i></div>
  </div>
  <div class="abs tile" style="left:472px;top:454px">
    <div class="photo" role="img" aria-label="Photo of a chrome mixer spigot" style="background:linear-gradient(135deg,#e6e7ea,#a9abb2 55%,#d4d5d9)"></div>
    <div class="cap"><b>Spigots</b><i>MORE</i></div>
  </div>
  <div class="abs tile" style="left:749px;top:454px">
    <div class="photo" role="img" aria-label="Photo of balustrade rail fittings" style="background:linear-gradient(#c9cacd,#f1f1f2 30%,#8f9095 70%,#b5b6ba)"></div>
    <div class="cap"><b>Balustrade Fittings</b><i>MORE</i></div>
  </div>
  <div class="abs tile" style="left:194px;top:618px">
    <div class="photo" role="img" aria-label="Photo of a glass facade against blue sky" style="background:linear-gradient(160deg,#d8eaf6,#7fb2db 45%,#2f6fa5)"></div>
    <div class="cap"><b>Glass</b><i>MORE</i></div>
  </div>
  <div class="abs tile" style="left:472px;top:618px">
    <div class="photo" role="img" aria-label="Photo of a round stainless glass fitting" style="background:radial-gradient(circle at 45% 50%,#e8e8ea,#8d8f94 55%,#c4c5c8)"></div>
    <div class="cap"><b>Glass fittings</b><i>MORE</i></div>
  </div>
  <div class="abs tile" style="left:749px;top:618px">
    <div class="photo" role="img" aria-label="Photo of aluminium U channels on dark background" style="background:linear-gradient(135deg,#2a2a2c,#9a9ca0 45%,#3a3a3d 75%,#1f1f21)"></div>
    <div class="cap"><b>Aluminium Channels</b><i>MORE</i></div>
  </div>
</section>

<section class="abs welcome">
  <h2>Welcome to our site</h2>
  <p>Lorem Ipsum is simply dummy text of the printing and typesetting industry. Lorem Ipsum has been the industry's standard dummy text ever since the 1500s, when an unknown printer took a galley of type and scrambled it to make a type specimen book. It has survived not only five centuries, but also the leap into electronic typesetting, remaining essentially unchanged.</p>
  <div class="abs people" role="img" aria-label="Photo of a smiling business team"></div>
</section>

<footer class="abs footer">
  <div class="abs footer-links">Home<span>|</span>About Us<span>|</span> Products<span>|</span>Download<span>|</span>Contact Us</div>
  <div class="abs copy">Copyrights @ 2013 All Rights Reserved</div>
  <div class="abs follow">Follow us On</div>
  <div class="abs social"><span></span><span></span><span></span></div>
</footer>

</body>
</html>
```